Skipper and fishing guide brochure

logo and brochure. Please see the word doc tobi 2 for brochure style. Please give me something unique and clean, not you typical fishing/boating logo. Tobias is a fishing guide and boat skipper. He moves some very expensive boats and helps people enjoy their very expensive toys. he works for people who have lots of money, toys and little time.

Target Market(s)

boat owners/buyers/boat sellers

Logo Text

Tobias Merlane

Requirements
Nice to have
• logo will be embroided on shirts and hats, would be nice to have some alternate colourways. EG on white, on grey and on black
Should not have
• trashy style font

```html
<!DOCTYPE html>
<html lang="en">
<head>
<meta charset="utf-8">
<title>Tobias Merlane – Fishing Guide Brochure</title>
<link href="https://fonts.googleapis.com/css2?family=Tinos:ital,wght@0,400;0,700;1,400;1,700&display=swap" rel="stylesheet">
<style>
  :root{
    --ink:#1a1d22;
    --sky-top:#c9dcef;
    --sky-mid:#a9c5e2;
    --sea:#6f93bd;
    --sea-deep:#4f77a6;
    --fold:#7f8fa3;
    --photo-top:#7fb3dc;
    --photo-mid:#3d8fc2;
    --photo-low:#4b8c55;
    --photo-fish:#8a5a36;
  }
  *{margin:0;padding:0;box-sizing:border-box}
  html,body{width:1200px;height:929px;overflow:hidden;background:#fff}
  .brochure{
    position:relative;width:1200px;height:929px;overflow:hidden;
    font-family:"Tinos","Times New Roman",serif;color:var(--ink);
  }
  .backdrop{
    position:absolute;inset:0;
    background:linear-gradient(180deg,var(--sky-top) 0%,var(--sky-mid) 30%,#9ab9d9 48%,var(--sea) 62%,var(--sea-deep) 100%);
  }
  .fold{position:absolute;top:0;bottom:0;border-left:1px dashed var(--fold);opacity:.55}
  .fold--one{left:400px}
  .fold--two{left:800px}
  .tagline{
    position:absolute;left:68px;top:36px;
    font-size:24px;font-weight:700;font-style:italic;white-space:nowrap;
  }
  .column{position:absolute;font-size:13px;line-height:15.4px}
  .column p{margin-bottom:15.4px}
  .column--left{left:33px;top:92px;width:356px}
  .column--mid{left:417px;top:92px;width:358px}
  .column--right{left:825px;top:148px;width:348px}
  .heading{
    font-size:19px;line-height:22px;font-weight:700;font-style:italic;text-decoration:underline;
    margin-bottom:14px;
  }
  .heading--plain{text-decoration:none;margin-bottom:10px}
  .services-title{
    text-align:center;font-size:19px;font-weight:700;font-style:italic;
    margin:34px 0 12px;
  }
  .web{position:absolute;left:33px;top:716px;width:356px;text-align:center;font-size:16px}
  .sponsor-label{position:absolute;left:33px;top:754px;font-size:16px;font-weight:700;font-style:italic}
  .sponsor-name{position:absolute;left:36px;top:788px;font-size:40px;font-weight:700;letter-spacing:1px}
  .brand{
    position:absolute;left:838px;top:34px;display:flex;align-items:center;gap:12px;
  }
  .brand-mark{width:16px;height:16px;background:var(--ink)}
  .brand-name{font-size:34px;font-weight:700;font-style:italic}
  .brand-role{font-size:14px;font-weight:700;font-style:italic;margin-top:2px}
  .lead{font-weight:700;font-style:italic;margin-bottom:54px !important}
  .photo{
    position:absolute;left:807px;top:394px;width:376px;height:480px;
    background:linear-gradient(180deg,var(--photo-top) 0%,#c8dfee 30%,var(--photo-mid) 48%,var(--photo-low) 72%,var(--photo-fish) 100%);
  }
</style>
</head>
<body>
<main class="brochure">
  <div class="backdrop" role="img" aria-label="Calm open ocean under a pale sky"></div>
  <div class="fold fold--one"></div>
  <div class="fold fold--two"></div>

  <h1 class="tagline">Work Hard, Stay Humble, Chase Your Dreams and GO Fishing…. That’s Me</h1>

  <section class="column column--left">
    <h2 class="heading">About Me:</h2>
    <p>I am what some would call borderline obsessed with the art of fishing. The fishing obsession spark ignited at the ripe old age of 3 when the old man(dad) took me fishing to a trout farm. In a defiant act of gently dropping the rod tip so the fish let go, I knew I could catch it again, and again. Next came the torture for my family of me watching a video called Shore Based Big Game Fishing, probably 1000 times. I just got lost in the moment over and over again watching Marlow Keats reel in that Cobia.</p>
    <p>Entering the epic world of boating and fishing with boundless purpose and passion with my first boat at 12 on the Gippsland Lakes in Victoria, I knew there was no going back. Mostly self-taught from there and armed with a shed full of the old man’s stiff old rods, Corvan reels and commitment, I ventured into that blue water toward chasing my dreams {and invested in some lighter tackle!}</p>
    <p>I relocated to the Sunshine Coast when I was 16, I discovered the pristine waters of the Noosa River, and the pelagics in the waters outside. This is where some of my best work happens. Even managed to get myself sponsored by Kestrel Tackle after an awesome hook up.</p>
    <p>I have spent the last 4 years guiding in the Great Barrier Reef whilst working on a live aboard charter vessel offering heavy tackle game fishing, light tackle sport fishing, spear fishing, right through to getting a feed of the tastiest fish the area has to offer. I am a universal angler and guide, and an experienced all-round boatman with an excessive amount of hours spent driving boats of all type’s.</p>
    <p>I have fished the entire east coast of Australia and am always on the pulse with what’s biting, where and when. I practice the catch and release method but if you want to keep them, then that’s ok too.</p>
    <p>When I’m not fishing, I am fishing for words on the keyboard writing articles about fishing…. Check them out if you like!</p>
  </section>
  <p class="web">https://www.reelfeed.net/tobimerlane/</p>
  <p class="sponsor-label">Sponsored by:</p>
  <p class="sponsor-name">KESTREL</p>

  <section class="column column--mid">
    <h2 class="heading">What You Can Expect:</h2>
    <p>Sunshine coast based, fishing obsessed Tobias Merlane has 4 years experience guiding the great barrier reef running 7 day live aboard charters offering a wide array of fishing types from heavy tackle game fishing, light tackle sport fishing right through to getting a feed of the tastiest fish the area has to offer.</p>
    <p>A universal angler and guide he has fished the entire east coast of Australia and is always on the pulse with whats biting, where and when. Tobias’ Trip planning, organization and communication skills ensure a safe and pleasurable trip.</p>
    <p class="services-title">~ SERVICES ~</p>
    <h2 class="heading heading--plain">Fishing:</h2>
    <p>Game fishing along the east coast of Australia has really taken off over the last ten years and for good reason. With different species popping their heads in to different locations all year round the crew can always find something to target. Setting off with a plan we head, search and and work as a team to do what we do best. Catch fish. Game fishing is a team sport, crew Tobias and Rhys mesh perfectly into a fish catching machine with more experience between then any others in the country. They have both been fortunate enough to be taught by some of the biggest names in fishing and have both now gone forward and continue to lead the recreational industry with international records and consistent personal captures that blow most peoples minds.</p>
    <p>Services also include pleasure cruises, vessel relocations and delivery’s.</p>
    <h2 class="heading heading--plain">Game Fishing Competitions:</h2>
    <p>Game fishing competitions are generally multi-day events with great atmosphere. We can crew your vessel to location if needed, during event and back afterward.</p>
    <p>If your not already, entry into competitions requires becoming a member of a club and fees normally start from $99pp. Only the angler needs to be a member of a NGFC affiliated club to enter your vessel in the running to possibly take out the win.</p>
    <p>For any further enquiries on game fishing competitions please contact Tobias - 0400 000 000.</p>
  </section>

  <div class="brand">
    <span class="brand-mark"></span>
    <div>
      <div class="brand-name">Tobias Merlane</div>
      <div class="brand-role">Tour Guide</div>
    </div>
  </div>

  <section class="column column--right">
    <p class="lead">Owner operated and hands on, I tailor the package to suit your request!</p>
    <p>The Bazaruto Archipelago has something to offer any fisherman all year round. Anglers come to enjoy light trolling for the big variety of pelagic game fish that frequent our shoreline. Popping and jigging for the many fish species that inhabit our healthy reef systems is also very popular.</p>
    <p>Come with your family and friends and catch the fish of your dreams.</p>
  </section>

  <div class="photo" role="img" aria-label="Split-level photo of an angler on a centre-console boat above the waterline and a large fish hooked on a lure below"></div>
</main>
</body>
</html>
```